Banners for Project Management Conference Social Media SItes

We are part of an established global professional project management organisation (QRV.net). We would be having our 21st project management conference in New Zealand this year and we are looking at a design of a series of banners that can be used across pagebook, chirplet and worknexa. The design of banners should express the theme of the conference, "Shaping the Future".

Our conference logo is as attached. The conference logo must be in the banner image and form part of the inspiration to the banner design.

The banners fitting pagebook, chirplet and worknexa should adhere to the banner sizing as follows.

1500x500px Chirplet banner
851x315px Pagebook banner
646x220px Worknexa banner

They should be of the same design, with minor adjustments to fit the dimensions indicated. As they are web components, 72dpi, RGB are standard requirements for the images.

Deliverables: 1 jpg of each type of banner. (3 in total)

Just a heads-up: The chirplet and pagebook banners would be partially blocked by its user-icon as shown in the two attached guide illustrations. Please make sure that the banner designed take into consideration of this and do not put in anything important (e.g. logo) in those spots.
Updates

Reason: Deadline extended because more interests have been registered. Thanks, guys.

Target Market(s)

Professional project managers, CEOs, Directors, managers in other fields.

Industry/Entity Type

Media

Requirements
Must have
• The conference logo must be part of the design of the banner. Would be great if the design can relate well with the logo.
Nice to have
• If stock images are needed to develop this banner, please inform.

```html
<!DOCTYPE html>
<html lang="en">
<head>
<meta charset="utf-8">
<title>Shaping the Future – New Zealand Conference Banner</title>
<link rel="stylesheet" href="https://fonts.googleapis.com/css2?family=Archivo+Black&family=Montserrat:wght@300;600&display=swap">
<style>
  :root {
    --mountain-light: #c9d9cf;
    --mountain-mid: #7f9e93;
    --mountain-deep: #2f4a48;
    --sky-teal: #5f8f8a;
    --city-glow: #b58a45;
    --ink: #111111;
    --paper: #ffffff;
    --piece: #2a2f2b;
    --piece-edge: #0c0e0c;
    --outline-cyan: #d9f4f2;
    --brand-green: #3d6b4a;
    --flag-blue: #24347a;
  }
  * { box-sizing: border-box; margin: 0; padding: 0; }
  html, body { width: 1200px; height: 444px; overflow: hidden; background: #ffffff; }
  .banner {
    position: relative;
    width: 1200px;
    height: 444px;
    overflow: hidden;
    font-family: "Archivo Black", "Arial Black", sans-serif;
  }
  .banner__backdrop {
    position: absolute;
    inset: 0;
    background:
      linear-gradient(90deg, rgba(47,74,72,0) 0%, rgba(47,74,72,0) 55%, rgba(29,43,46,0.35) 75%, rgba(29,43,46,0.6) 100%),
      radial-gradient(ellipse 30% 40% at 88% 95%, rgba(181,138,69,0.55), transparent 70%),
      linear-gradient(180deg, var(--sky-teal) 0%, var(--mountain-light) 30%, var(--mountain-mid) 60%, var(--mountain-deep) 100%);
  }
  .conference-mark {
    position: absolute;
    left: 21px;
    top: 15px;
    display: flex;
    align-items: center;
    gap: 14px;
  }
  .conference-mark__dot {
    width: 76px;
    height: 76px;
    border-radius: 50%;
    background: var(--brand-green);
  }
  .conference-mark__name {
    font-family: "Montserrat", sans-serif;
    font-weight: 600;
    font-size: 19px;
    line-height: 1.15;
    color: var(--brand-green);
    width: 100px;
  }
  .headline { font-size: inherit; font-weight: normal; }
  .headline__word {
    position: absolute;
    color: var(--ink);
    -webkit-text-stroke: 2px var(--paper);
    paint-order: stroke fill;
    text-shadow: 0 0 3px var(--paper);
    line-height: 1;
    white-space: nowrap;
  }
  .headline__word--shaping { left: 329px; top: 117px; font-size: 52px; letter-spacing: -1.5px; }
  .headline__word--the { left: 404px; top: 210px; font-size: 50px; }
  .puzzle-row {
    position: absolute;
    left: 543px;
    display: flex;
    gap: 4px;
  }
  .puzzle-row--top { top: 127px; }
  .puzzle-row--bottom { top: 198px; }
  .puzzle-piece {
    width: 100px;
    height: 64px;
    background: var(--piece);
    border: 2px solid var(--piece-edge);
    border-radius: 8px;
    display: flex;
    align-items: center;
    justify-content: center;
    font-size: 44px;
    color: var(--piece);
    -webkit-text-stroke: 2px var(--paper);
    line-height: 1;
  }
  .puzzle-row--bottom .puzzle-piece { width: 103px; height: 76px; }
  .flag-pole {
    position: absolute;
    left: 367px;
    top: 276px;
    width: 3px;
    height: 150px;
    background: linear-gradient(180deg, #e6e6e6, rgba(230,230,230,0));
  }
  .flag {
    position: absolute;
    left: 370px;
    top: 279px;
    width: 70px;
    height: 42px;
    background: var(--flag-blue);
  }
  .country {
    position: absolute;
    left: 368px;
    top: 346px;
    width: 520px;
    height: 66px;
    overflow: visible;
  }
  .country__text {
    font-family: "Montserrat", sans-serif;
    font-weight: 300;
    font-size: 56px;
    fill: transparent;
    stroke: var(--outline-cyan);
    stroke-width: 1.3px;
    filter: drop-shadow(0 0 4px rgba(217,244,242,0.55));
  }
</style>
</head>
<body>
  <div class="banner">
    <div class="banner__backdrop" role="img" aria-label="Photo of snow-capped New Zealand mountains on the left blending into a dusk city skyline with a tall observation tower on the right"></div>

    <div class="conference-mark">
      <span class="conference-mark__dot"></span>
      <span class="conference-mark__name">Horizon Forum</span>
    </div>

    <h1 class="headline">
      <span class="headline__word headline__word--shaping">Shaping</span>
      <span class="headline__word headline__word--the">The</span>
      <span class="puzzle-row puzzle-row--top">
        <span class="puzzle-piece">F</span>
        <span class="puzzle-piece">U</span>
        <span class="puzzle-piece">T</span>
      </span>
      <span class="puzzle-row puzzle-row--bottom">
        <span class="puzzle-piece">U</span>
        <span class="puzzle-piece">R</span>
        <span class="puzzle-piece">E</span>
      </span>
    </h1>

    <span class="flag-pole"></span>
    <div class="flag" role="img" aria-label="New Zealand flag on a pole"></div>

    <svg class="country" viewBox="0 0 520 66" aria-label="New Zealand">
      <text class="country__text" x="2" y="58" textLength="512" lengthAdjust="spacing">NEWZEALAND</text>
    </svg>
  </div>
</body>
</html>
```